Software Company Business Card Design

We are looking for a business card design for a software, messaging & IT services company based in Australia.

Lumora Group is the holding company for 3 brands all offering technology based business solutions; Lumora, Velbrix & Quillray. Brand Identity = Friendly, Professional, Viable, Vibrant, Creative

We want our business card to reflect that we are an innovative market leader. The design should be clean, professional and original.

This design will be used for all 3 brands.

More information about our company can be found at: www.lumoragroup-example.com.au
www.velbrix-example.com.au

Details we would like on the card:

Firstname Lastname
Position
Level 17, 248 Tarrow St
North Sydney
NSW 2060
Phone: +61 2 9387 2600
Fax: +61 2 9387 2611
Mobile:
Email:
www.lumoragroup-example.com.au

Target Market(s)

Our business cards are given to B2B and industry professionals.

Industry/Entity Type

Business

Requirements
Must have
• The Business Card must include the same colours as the logo.
Nice to have
• We would like it to me double sided.

```html
<!DOCTYPE html>
<html lang="en">
<head>
<meta charset="utf-8">
<title>Lumora Group – Business Card</title>
<link rel="stylesheet" href="https://fonts.googleapis.com/css2?family=Gelasio:wght@400;500&family=Tinos&display=swap">
<style>
  :root {
    --crimson: #ad1442;
    --crimson-soft: #d9707f;
    --slate: #8e90ae;
    --ink: #111111;
    --paper: #ffffff;
    --edge: #e3e3e8;
  }
  * { box-sizing: border-box; margin: 0; padding: 0; }
  html, body { width: 793px; height: 1200px; overflow: hidden; background: var(--paper); }
  .canvas { position: relative; width: 793px; height: 1200px; }

  .side-label {
    position: absolute;
    font-family: "Tinos", "Times New Roman", serif;
    font-size: 27px;
    color: var(--ink);
  }
  .side-label--front { left: 74px; top: 34px; }
  .side-label--back { left: 90px; top: 650px; }

  .card {
    position: absolute;
    width: 665px;
    height: 406px;
    border: 1px solid var(--edge);
    border-radius: 26px;
    overflow: hidden;
    background: var(--paper);
  }
  .card--front { left: 50px; top: 120px; }
  .card--back { left: 74px; top: 735px; height: 408px; }

  /* Front */
  .wordmark {
    position: absolute;
    left: 98px;
    top: 108px;
    font-family: "Gelasio", Georgia, serif;
    font-weight: 500;
    font-size: 86px;
    line-height: 1;
    color: var(--crimson);
    letter-spacing: 1px;
  }
  .front-band {
    position: absolute;
    left: 0; right: 0; bottom: 0;
    height: 66px;
    background: var(--crimson);
  }
  .website {
    position: absolute;
    left: 66px;
    top: 18px;
    font-family: "Gelasio", Georgia, serif;
    font-size: 19px;
    letter-spacing: 3.6px;
    color: var(--paper);
  }
  .band-bars { position: absolute; right: 0; top: 0; height: 66px; width: 150px; }

  /* Back */
  .back-band {
    position: absolute;
    left: 0; top: 0;
    width: 520px;
    height: 120px;
    background: var(--crimson);
  }
  .back-bars { position: absolute; left: 533px; top: 0; width: 132px; height: 120px; }
  .holder-name {
    position: absolute;
    right: 6px;
    top: 30px;
    font-family: "Gelasio", Georgia, serif;
    font-size: 29px;
    color: var(--paper);
    white-space: nowrap;
  }
  .holder-position {
    position: absolute;
    right: 8px;
    top: 73px;
    font-family: "Gelasio", Georgia, serif;
    font-size: 18px;
    letter-spacing: 5px;
    color: #e7c2cb;
  }
  .contact {
    position: absolute;
    left: 0; right: 90px;
    top: 320px;
    text-align: center;
    font-family: "Gelasio", Georgia, serif;
    font-size: 16.5px;
    line-height: 23px;
    color: var(--crimson);
  }
  .contact .label { color: var(--slate); }
</style>
</head>
<body>
<div class="canvas">
  <div class="side-label side-label--front">Front</div>

  <section class="card card--front">
    <div class="wordmark">Lumora Group</div>
    <div class="front-band">
      <div class="website">www.lumoragroup-example.com.au</div>
      <svg class="band-bars" viewBox="0 0 150 66" aria-hidden="true">
        <rect x="13" y="0" width="9" height="66" fill="#ffffff"/>
        <rect x="57" y="0" width="8" height="66" fill="#ffffff"/>
        <rect x="107" y="0" width="8" height="66" fill="#ffffff"/>
      </svg>
    </div>
  </section>

  <div class="side-label side-label--back">Back side of the card</div>

  <section class="card card--back">
    <div class="back-band">
      <div class="holder-name">Firstname Lastname</div>
      <div class="holder-position">Position</div>
    </div>
    <svg class="back-bars" viewBox="0 0 132 120" aria-hidden="true">
      <rect x="0" y="0" width="41" height="120" fill="#ad1442"/>
      <rect x="53" y="0" width="40" height="120" fill="#ad1442"/>
      <rect x="103" y="0" width="29" height="120" fill="#ad1442"/>
    </svg>
    <address class="contact" style="font-style: normal;">
      Level 17, 248 Tarrow St / North Sydney / NSW 2060<br>
      <span class="label">Ph:</span> +61 2 9387 2600 <span class="label">/ F:</span> +61 2 9387 2611 <span class="label">/ M:</span> 0400 000 000<br>
      <span class="label">E-mail:</span> abc@lumoragroup-example.com.au
    </address>
  </section>
</div>
</body>
</html>
```